Web Design Project

i'm looking for a sleek modern design i can use for a web site that deals with.
Intelligent Data Capture
Accounts Payable Solutions for faster processing based on our scanning solution.
ultimately we are a intelligent scanning software.

here is a great website, that does exactly what we do, and we like to have most of their services and products.

so something in this idea would be great.
www.varnol.com

so i guess i want a good landing/home page which is smartly designed so users will be inclined to leave their information.

and then information pages.

also i dont need any cms for you to include, i only need you to hook the html hooks for RANK Kettle as i already have a CMS and need it to hook in to that, i am including links to that cheat sheet.
so it is easier when included as you create the Theme.

http://www.rankkettle.com/how-to-create-website-template.html
http://www.rankkettle.com/cheat-sheet.html
Updates

Hi Guys sorry for the long pause in design, but here is where we stand.

what ever design i choose, i need that designer to customize a few things for me based on design that was designed.
and i will need designer to match that them to work with RANK Kettle
here is the cheat sheet for the hooks that we need to match and make it work.
if you have any questions let me know.

otherwise i look forward to working with you. and good luck.

Target Market(s)

CFO's AP Managers, mostly ppl who are not Tech freindly

Industry/Entity Type

Software

Requirements
Must have
• i need on home page, the rotating banner should have 1 ability to place clipvane links to show videos, and also ability to add buttons on these rotating banners that will allow forms to pop up take to another page.

```html
<!DOCTYPE html>
<html lang="en">
<head>
<meta charset="utf-8">
<title>Intelligent Data Capture – Home</title>
<link rel="stylesheet" href="https://fonts.googleapis.com/css2?family=Cinzel:wght@400;600&family=Mulish:wght@400;700&family=Open+Sans:wght@600;700&family=Tinos:ital@0;1&display=swap">
<style>
  :root {
    --ink-dark: #262626;
    --page-grey: #c9c9c9;
    --card-grey: #dcdcdc;
    --band-grey: #d8d8d8;
    --accent-orange: #ec950a;
    --service-blue: #2a33a3;
    --logo-ink: #c9d2d8;
    --nav-ink: #7a7a7a;
    --text-ink: #2b2b2b;
    --white: #ffffff;
  }
  * { box-sizing: border-box; margin: 0; padding: 0; }
  html, body { width: 1000px; height: 1200px; overflow: hidden; }
  body {
    position: relative;
    background: var(--page-grey);
    font-family: "Mulish", sans-serif;
    color: var(--text-ink);
  }

  /* ---------- header ---------- */
  .site-header {
    position: absolute; left: 0; top: 0; width: 1000px; height: 340px;
    background: var(--ink-dark);
  }
  .accent-strip {
    position: absolute; left: 0; top: 340px; width: 1000px; height: 10px;
    background: var(--accent-orange);
  }
  .brand {
    position: absolute; left: 52px; top: 24px;
    font-family: "Tinos", serif; font-size: 39px; color: var(--logo-ink);
    letter-spacing: 0.5px;
  }
  .search {
    position: absolute; left: 729px; top: 29px; width: 223px; height: 37px;
    border-radius: 19px; border: 2px solid #d8d8d8;
    background: linear-gradient(#9a9a9a, #7d7d7d);
  }
  .search-field {
    position: absolute; left: 16px; top: 6px;
    font-family: "Tinos", serif; font-style: italic; font-size: 19px; color: #e6e6e6;
  }
  .search-button {
    position: absolute; right: -2px; top: -2px; width: 45px; height: 37px;
    border-radius: 19px; background: #d7232b; border: 2px solid #d8d8d8;
  }
  .search-button svg { position: absolute; left: 11px; top: 7px; }

  /* ---------- navigation ---------- */
  .main-nav {
    position: absolute; left: 49px; top: 100px; width: 901px; height: 40px;
    border-radius: 6px 6px 0 0;
    background: linear-gradient(#ffffff, #e4e4e4);
    display: flex; align-items: center;
  }
  .nav-item {
    font-family: "Cinzel", serif; font-size: 19px; color: var(--nav-ink);
    position: absolute; top: 8px; white-space: nowrap;
  }
  .nav-item.is-current {
    top: 5px; padding: 1px 5px 2px;
    background: var(--accent-orange); color: var(--white);
    border: 2px solid #f7d08a; border-radius: 3px;
    box-shadow: 1px 2px 3px rgba(0,0,0,.4);
  }

  /* ---------- banner ---------- */
  .service-list { position: absolute; left: 49px; top: 139px; width: 311px; height: 211px; }
  .service-tab {
    position: absolute; left: 0; width: 311px; height: 53px;
    background: linear-gradient(#c4c4c4, #9a9a9a);
    border-top: 1px solid #d8d8d8;
    font-family: "Mulish", sans-serif; font-size: 29px; color: var(--white);
    padding: 8px 0 0 18px; text-shadow: 1px 1px 2px rgba(0,0,0,.55);
  }
  .service-tab.is-active { background: var(--service-blue); border-top: none; padding-top: 13px; height: 62px; }
  .service-pointer { position: absolute; left: 360px; top: 139px; }
  .banner-visual {
    position: absolute; left: 360px; top: 139px; width: 590px; height: 211px;
    background: linear-gradient(120deg, #3c5a62 0%, #a9d2d8 30%, #e8f2f2 50%, #6c9aa2 72%, #2e3e44 100%);
  }
  .banner-caption {
    position: absolute; left: 360px; top: 300px; width: 590px; height: 50px;
    background: rgba(40,40,40,.85);
    font-size: 17px; line-height: 20px; color: var(--white);
    padding: 5px 12px 0 12px; letter-spacing: .2px;
  }

  /* ---------- feature cards ---------- */
  .feature-card {
    position: absolute; top: 374px; width: 282px; height: 478px;
    background: var(--card-grey);
    box-shadow: 0 0 6px rgba(0,0,0,.25);
    text-align: center;
  }
  .feature-title { margin-top: 10px; font-size: 41px; font-weight: 700; line-height: 46px; color: #2a2a2a; }
  .feature-subtitle { font-size: 26px; line-height: 30px; color: #2f2f2f; }
  .feature-visual {
    margin: 14px auto 0; width: 256px; height: 188px;
    background: linear-gradient(160deg, #e8f0f6 0%, #b3cde0 55%, #6e95b6 100%);
  }
  .feature-text { text-align: left; margin: 30px 0 0 14px; font-size: 18px; line-height: 25px; color: #2c2c2c; }
  .feature-text p + p { margin-top: 25px; }

  /* ---------- clients & footer ---------- */
  .clients-band {
    position: absolute; left: 0; top: 881px; width: 1000px; height: 73px;
    border-top: 1px solid #555; background: var(--band-grey);
  }
  .clients-title {
    position: absolute; left: 22px; top: 12px;
    font-family: "Tinos", serif; font-style: italic; font-size: 31px; color: #2d2d2d;
  }
  .lower-panel {
    position: absolute; left: 0; top: 954px; width: 1000px; height: 200px;
    background: var(--ink-dark);
  }
  .panel-fold { position: absolute; top: 937px; }
  .panel-tab {
    position: absolute; top: 937px; width: 244px; height: 77px;
    background: var(--accent-orange);
    font-family: "Open Sans", sans-serif; font-weight: 700; font-size: 23px; color: var(--white);
    display: flex; align-items: center; justify-content: center;
  }
  .panel-text {
    position: absolute; top: 1042px; width: 250px;
    font-family: "Open Sans", sans-serif; font-weight: 700; font-size: 13.4px; line-height: 17px; color: var(--white);
  }
  .site-footer {
    position: absolute; left: 0; top: 1154px; width: 1000px; height: 46px;
    background: #d6d6d6; text-align: center;
    font-family: "Tinos", serif; font-size: 21px; line-height: 46px; color: #222;
  }
</style>
</head>
<body>

<header class="site-header">
  <div class="brand">Company Logo</div>
  <div class="search">
    <span class="search-field">Search ....</span>
    <span class="search-button">
      <svg width="20" height="20" viewBox="0 0 20 20"><circle cx="7" cy="7" r="5" fill="none" stroke="#2a0a0a" stroke-width="2.5"/><line x1="11" y1="11" x2="18" y2="17" stroke="#2a0a0a" stroke-width="3" stroke-linecap="round"/></svg>
    </span>
  </div>
</header>
<div class="accent-strip"></div>

<nav class="main-nav">
  <span class="nav-item is-current" style="left:20px">Home Page</span>
  <span class="nav-item" style="left:181px">About Us</span>
  <span class="nav-item" style="left:321px">Portfolio</span>
  <span class="nav-item" style="left:470px">Services</span>
  <span class="nav-item" style="left:598px">Our Team</span>
  <span class="nav-item" style="left:736px">Contact Us</span>
</nav>

<div class="banner-visual" role="img" aria-label="Close-up photo of filed paper folders in a cabinet"></div>
<div class="banner-caption">Accounts Payable Solutions for faster processing based on our scanning solution</div>

<div class="service-list">
  <div class="service-tab" style="top:53px">Service 2</div>
  <div class="service-tab" style="top:102px">Service 3</div>
  <div class="service-tab" style="top:152px;height:59px;padding-top:13px">Service 4</div>
  <div class="service-tab is-active" style="top:0">Service 1</div>
</div>
<svg class="service-pointer" width="24" height="62" viewBox="0 0 24 62"><polygon points="0,0 22,31 0,62" fill="#2a33a3"/></svg>

<section class="feature-card" style="left:59px">
  <h2 class="feature-title">About Us</h2>
  <div class="feature-subtitle">What we do</div>
  <div class="feature-visual" role="img" aria-label="Illustration of a hand reaching toward a tablet with data pixels and gears"></div>
  <div class="feature-text"><p>Hi My name is Rehan, and I am freelance Graphics and Web Lay out designer.</p><p>If you need any changes tell me i am here to do it.</p></div>
</section>
<section class="feature-card" style="left:360px">
  <h2 class="feature-title">Contact Us</h2>
  <div class="feature-subtitle">How to Meet Us</div>
  <div class="feature-visual" role="img" aria-label="Illustration of a hand reaching toward a tablet with data pixels and gears"></div>
  <div class="feature-text"><p>Hi My name is Rehan, and I am freelance Graphics and Web Lay out designer.</p><p>If you need any changes tell me i am here to do it.</p></div>
</section>
<section class="feature-card" style="left:658px">
  <h2 class="feature-title">Why Us</h2>
  <div class="feature-subtitle">Why Choose Us</div>
  <div class="feature-visual" role="img" aria-label="Illustration of a hand reaching toward a tablet with data pixels and gears"></div>
  <div class="feature-text"><p>Hi My name is Rehan, and I am freelance Graphics and Web Lay out designer.</p><p>If you need any changes tell me i am here to do it.</p></div>
</section>

<section class="clients-band"><h2 class="clients-title">OUR CLIENTS</h2></section>
<section class="lower-panel"></section>

<svg class="panel-fold" style="left:57px" width="10" height="18"><polygon points="10,0 10,18 0,18" fill="#5c5c5c"/></svg>
<svg class="panel-fold" style="left:311px" width="10" height="18"><polygon points="0,0 10,18 0,18" fill="#5c5c5c"/></svg>
<svg class="panel-fold" style="left:368px" width="10" height="18"><polygon points="10,0 10,18 0,18" fill="#5c5c5c"/></svg>
<svg class="panel-fold" style="left:622px" width="10" height="18"><polygon points="0,0 10,18 0,18" fill="#5c5c5c"/></svg>
<svg class="panel-fold" style="left:678px" width="10" height="18"><polygon points="10,0 10,18 0,18" fill="#5c5c5c"/></svg>
<svg class="panel-fold" style="left:932px" width="10" height="18"><polygon points="0,0 10,18 0,18" fill="#5c5c5c"/></svg>

<div class="panel-tab" style="left:67px">News And Updates</div>
<div class="panel-tab" style="left:378px">Latest Blog Post</div>
<div class="panel-tab" style="left:688px">Recent Comments</div>

<p class="panel-text" style="left:68px">Hey, my name is Rehan Malik and I am doing my Graduation From NCT - IBS in Media Technology.</p>
<p class="panel-text" style="left:380px">Hey, my name is Rehan Malik and I am doing my Graduation From NCT - IBS in Media Technology.</p>
<p class="panel-text" style="left:688px">Hey, my name is Rehan Malik and I am doing my Graduation From NCT - IBS in Media Technology.</p>

<footer class="site-footer">Copyright © LQS 2012</footer>

</body>
</html>
```